Where Does The River Bend? Nine Keys For A Brighter Path

The book is about the metaphorical backpack we each carry from the day we are born. In it we accumulate a lifetime of experiences, memories, emotions and beliefs. This can weigh us down and hamper us from living a truly abundant life. The book invites the reader to put down their backpack and look inside to see what can stay and what can be let go. I am creating a new cover for the book for printing and distribution in India.

I see on the cover one person who has put her backpack on the floor and is looking inside it. Another person is plodding on weighed down by the burden of their heavy backpack. I would like to be a backdrop that shows nature as a metaphor for people travelling on the journey that is life.

The book has already been published and is readily available in all regions but India. So I am looking to create a different cover for the Indian market. I won't upload the existing cover because I would like the artist to bring their own fresh perspective on this topic.

```html
<!DOCTYPE html>
<html lang="en">
<head>
<meta charset="utf-8">
<title>Where Does The River Bend? – Book Cover</title>
<link rel="stylesheet" href="https://fonts.googleapis.com/css2?family=Anton&family=Oswald:wght@600&family=Montserrat:wght@400;500&display=swap">
<style>
  :root {
    --page-bg: #f3f1ed;
    --cover-bg: #dfe6f2;
    --navy: #2c3a78;
    --accent-yellow: #f2c350;
    --sky-light: #e4ebf6;
    --hill-soft: #b9cfc4;
    --river-blue: #8ea7d6;
    --figure-light: #9fb2de;
    --figure-dark: #5c73b8;
  }
  * { box-sizing: border-box; margin: 0; padding: 0; }
  html, body {
    width: 1200px;
    height: 730px;
    overflow: hidden;
    background: var(--page-bg);
  }
  .canvas {
    width: 1200px;
    height: 730px;
    display: flex;
    align-items: center;
    justify-content: center;
  }
  .book-cover {
    position: relative;
    width: 468px;
    height: 700px;
    overflow: hidden;
    background: var(--cover-bg);
    color: var(--navy);
  }
  .nature-backdrop {
    position: absolute;
    left: 0;
    right: 0;
    top: 300px;
    bottom: 0;
    background: linear-gradient(180deg, var(--cover-bg) 0%, var(--sky-light) 22%, var(--hill-soft) 58%, var(--river-blue) 100%);
    opacity: 0.7;
  }
  .cover-content {
    position: relative;
    height: 100%;
    display: flex;
    flex-direction: column;
    align-items: center;
    padding: 40px 30px 34px;
  }
  .book-title {
    font-family: "Anton", sans-serif;
    font-weight: 400;
    font-size: 76px;
    line-height: 0.98;
    letter-spacing: 0;
    text-transform: uppercase;
    text-align: center;
  }
  .book-title span { display: block; }
  .book-subtitle {
    margin-top: 12px;
    padding: 6px 8px 5px;
    border-top: 2px solid var(--accent-yellow);
    border-bottom: 2px solid var(--accent-yellow);
    font-family: "Montserrat", sans-serif;
    font-weight: 500;
    font-size: 18px;
    letter-spacing: 0.5px;
    text-align: center;
  }
  .journey-scene {
    margin-top: 26px;
    width: 320px;
    height: 200px;
    border-radius: 24px;
    background: linear-gradient(160deg, var(--figure-light), var(--figure-dark));
    opacity: 0.9;
  }
  .author-name {
    margin-top: auto;
    font-family: "Oswald", sans-serif;
    font-weight: 600;
    font-size: 42px;
    line-height: 1.1;
    letter-spacing: 4px;
    text-transform: uppercase;
  }
  .illustrator-credit {
    margin-top: 4px;
    font-family: "Montserrat", sans-serif;
    font-weight: 400;
    font-size: 15px;
    letter-spacing: 0.4px;
  }
</style>
</head>
<body>
  <main class="canvas">
    <article class="book-cover">
      <div class="nature-backdrop" role="img" aria-label="Nature backdrop: soft hills and a winding river as a metaphor for life's journey"></div>
      <div class="cover-content">
        <h1 class="book-title">
          <span>Where Does</span>
          <span>The River</span>
          <span>Bend?</span>
        </h1>
        <p class="book-subtitle">Nine Keys For A Brighter Path</p>
        <div class="journey-scene" role="img" aria-label="Illustration: a woman kneeling beside her open backpack looking inside it, while another traveller plods on bent under a heavy backpack"></div>
        <p class="author-name">Meera Kashyap</p>
        <p class="illustrator-credit">Illustrations by Arjun Kashyap</p>
      </div>
    </article>
  </main>
</body>
</html>
```